Professional Financial services company want to rebrand their stationary

We need stationary design for Veltor Group, its a company with 4 member companys that include Veltor Auditing, Veltor Financial Consultancy, Veltor Debt Collection and Veltor Real Estate.

We are based in dubai so the designers need to keep in mind that we use both english and arabic so leave a space for the arabic writing.

We recently redesigned our Logo and would like to redesign our stationary to go along with it.

You will find attached the logo, please keep it looking professional and use the logo as a guide for colors when designing.

Good luck to everyone

Industry/Entity Type

Finance And Accounting

Font styles to use
Sans Serif

Colors
0292cd
33a6d7
3276b5
0355a3
ffffff
dbdbdb

Requirements
Must have
• Letterhead
• Business card
• Envelope small and A4
Nice to have
• Professional
• Space for Arabic and english

```html
<!DOCTYPE html>
<html lang="en">
<head>
<meta charset="utf-8">
<title>Veltor Group Stationery</title>
<link href="https://fonts.googleapis.com/css2?family=Montserrat:wght@400;500;600&display=swap" rel="stylesheet">
<style>
  :root {
    --brand-blue: #0f6db7;
    --band-grey: #6d6e70;
    --ink: #3a3a3c;
    --paper: #ffffff;
    --backdrop: #bdbdbd;
  }
  * { box-sizing: border-box; margin: 0; padding: 0; }
  html, body { width: 1200px; height: 1200px; overflow: hidden; }
  body {
    position: relative;
    background: radial-gradient(circle at 50% 40%, #c9c9c9, #b4b4b4);
    font-family: "Montserrat", sans-serif;
    color: var(--ink);
  }
  .sheet { position: absolute; background: var(--paper); box-shadow: 4px 6px 12px rgba(0,0,0,.28); overflow: hidden; }
  .brand { display: flex; align-items: center; gap: .35em; font-weight: 600; color: var(--brand-blue); white-space: nowrap; letter-spacing: -.01em; }
  .brand-square { width: .8em; height: .8em; background: currentColor; display: block; }
  .brand.on-blue { color: var(--paper); }
  .band { position: absolute; left: 0; width: 100%; }
  .band svg { position: absolute; inset: 0; width: 100%; height: 100%; }
  .band-url { position: absolute; color: var(--paper); font-weight: 600; letter-spacing: .12em; }

  /* Letterhead */
  .letterhead { left: 77px; top: 67px; width: 766px; height: 1077px; z-index: 1; }
  .letterhead .brand { position: absolute; left: 69px; top: 84px; font-size: 29px; }
  .letter-date { position: absolute; left: 96px; top: 216px; font-size: 14px; }
  .letter-body { position: absolute; left: 96px; top: 285px; width: 600px; font-size: 13.4px; line-height: 16.5px; text-align: justify; }
  .letter-body p { text-indent: 40px; margin-bottom: 16.5px; }
  .letter-contacts { position: absolute; left: 183px; top: 992px; display: flex; gap: 12px; font-size: 13px; align-items: center; }
  .contact { display: flex; align-items: center; gap: 4px; }
  .contact svg { fill: var(--brand-blue); }
  .letterhead .band { top: 1019px; height: 58px; }
  .letterhead .band-url { right: 45px; top: 19px; font-size: 14px; }

  /* Business cards */
  .card { left: 802px; width: 323px; height: 206px; z-index: 2; }
  .card-front { top: 101px; }
  .card-front .brand { position: absolute; left: 13px; top: 38px; font-size: 17px; }
  .card-holder { position: absolute; right: 17px; top: 82px; text-align: right; }
  .card-holder .name { font-size: 11.5px; font-weight: 500; }
  .card-holder .role { font-size: 8.5px; }
  .card-tab { position: absolute; right: 0; top: 79px; width: 13px; height: 30px; background: var(--brand-blue); }
  .card-contacts { position: absolute; left: 15px; top: 124px; font-size: 8.5px; line-height: 13px; }
  .card-address { position: absolute; right: 18px; top: 121px; text-align: right; font-size: 8.5px; line-height: 10px; }
  .card-front .band { top: 186px; height: 20px; }
  .card-front .band-url { right: 17px; top: 4px; font-size: 9.5px; }
  .card-back { top: 330px; height: 212px; background: var(--brand-blue); }
  .card-back .brand { position: absolute; left: 50%; top: 50%; transform: translate(-50%,-50%); font-size: 19px; }

  /* Envelope back with flap */
  .envelope-back { left: 48px; top: 698px; width: 667px; height: 333px; z-index: 3; }
  .envelope-flap { position: absolute; left: 0; top: 0; width: 100%; height: 105px; }
  .envelope-back .brand { position: absolute; left: 262px; top: 40px; font-size: 22px; }

  /* Envelope front */
  .envelope-front { left: 494px; top: 570px; width: 668px; height: 334px; z-index: 4; }
  .envelope-front .brand { position: absolute; left: 31px; top: 52px; font-size: 29px; }
  .envelope-address { position: absolute; left: 34px; top: 240px; font-size: 10.4px; line-height: 13px; }
  .envelope-front .band { top: 301px; height: 33px; }
  .envelope-front .band-url { right: 20px; top: 8px; font-size: 13.5px; }
</style>
</head>
<body>

<section class="sheet letterhead" aria-label="Letterhead">
  <div class="brand"><span class="brand-square"></span>VELTOR GROUP</div>
  <p class="letter-date">15 November 2017</p>
  <div class="letter-body">
    <p>Lorem ipsum dolor sit amet, consectetur adipiscing elit. Suspendisse condimentum egestas tellus et viverra. Vestibulum euismod lacus eget nisi ornare, id laoreet tortor dapibus. Donec lacinia euismod diam, convallis tempus risus, ut et felis tempor eros blandit feugiat ut non enim. In vestibulum ligula blandit magna blandit dictum. Sed malesuada erat id mauris pretium, et congue felis interdum. Aenean ultricies enim nec lorem vestibulum, nec commodo quam sagittis. Cras bibendum mauris, eget aliquet semper, libero ipsum ultricies nunc, euismod pellentesque orci risus amet nibh. Maecenas feugiat mi a metus convallis pharetra.</p>
    <p>Duis porta turpis ut pulvinar hendrerit elit lorem vehicula turpis, lacinia semper purus ros ac nisi. Sed consectetur ante scelerisque tortor pellentesque imperdiet. Pellentesque habitant morbi tristique senectus et netus et malesuada fames ac turpis egestas. Quisque justo turpis, varius ante nec, tincidunt pharetra tellus. Donec non euismod est. Nulla in elit quis tellus mattis feugiat vitae vitae ut magna. Etiam at nisi quis dolor lacinia hendrerit placerat et risus. Vestibulum ac sapien ut justo varius venenatis.</p>
    <p>Donec eget nunc bibendum, sodales augue in, morbi tristique senectus et netus et malesuada fames varius ante nec, accumsan ultricies magna. Mauris pharetra tellus. Donec non euismod est.<br>Mauris vitae orci augue. Duis sit amet erat id lectus.</p>
  </div>
  <div class="letter-contacts">
    <span class="contact"><svg width="14" height="11" viewBox="0 0 14 11"><path d="M1 4c0-3 12-3 12 0l-2 1-2-1V3H5v1L3 5zM3 6h8l1 5H2z"/></svg>+971 00 000000</span>
    <span class="contact"><svg width="9" height="13" viewBox="0 0 9 13"><path d="M1 0h7v13H1zM2 1.5v9h5v-9z"/></svg>+971 00 000000</span>
    <span class="contact"><svg width="13" height="9" viewBox="0 0 13 9"><path d="M0 0h13v9H0zM1 1l5.5 4L12 1z"/></svg>&nbsp;name@veltorgroup.com</span>
  </div>
  <div class="band">
    <svg viewBox="0 0 766 58" preserveAspectRatio="none"><rect width="766" height="58" fill="var(--band-grey)"/><polygon points="0,0 292,0 272,58 0,58" fill="var(--brand-blue)"/><polygon points="292,0 302,0 282,58 272,58" fill="#fff"/></svg>
    <span class="band-url">www.veltorgroup.com</span>
  </div>
</section>

<section class="sheet card card-front" aria-label="Business card front">
  <div class="brand"><span class="brand-square"></span>VELTOR GROUP</div>
  <div class="card-holder"><div class="name">First Name, Last Name</div><div class="role">Director</div></div>
  <div class="card-tab"></div>
  <div class="card-contacts">
    <div>+971 00 000000</div><div>+971 00 000000</div><div>name@veltorgroup.com</div>
  </div>
  <div class="card-address">Address 1, Address 2<br>Address 3, Address 4<br>Street Name, Street Name</div>
  <div class="band">
    <svg viewBox="0 0 323 20" preserveAspectRatio="none"><rect width="323" height="20" fill="var(--band-grey)"/><polygon points="0,0 124,0 115,20 0,20" fill="var(--brand-blue)"/><polygon points="124,0 129,0 120,20 115,20" fill="#fff"/></svg>
    <span class="band-url">www.veltorgroup.com</span>
  </div>
</section>

<section class="sheet card card-back" aria-label="Business card back">
  <div class="brand on-blue"><span class="brand-square"></span>VELTOR GROUP</div>
</section>

<section class="sheet envelope-back" aria-label="Envelope back">
  <svg class="envelope-flap" viewBox="0 0 667 105" preserveAspectRatio="none"><path d="M0 0H667V105H50C25 105 14 92 10 70L0 0Z" fill="var(--brand-blue)"/></svg>
  <div class="brand on-blue"><span class="brand-square"></span>VELTOR GROUP</div>
</section>

<section class="sheet envelope-front" aria-label="Envelope front">
  <div class="brand"><span class="brand-square"></span>VELTOR GROUP</div>
  <div class="envelope-address">Address 1, Address 2<br>Address 3, Address 4<br>Street Name, Street Name<br>Street Name, Zip Code 00000</div>
  <div class="band">
    <svg viewBox="0 0 668 33" preserveAspectRatio="none"><rect width="668" height="33" fill="var(--band-grey)"/><polygon points="0,0 223,0 214,33 0,33" fill="var(--brand-blue)"/><polygon points="223,0 231,0 222,33 214,33" fill="#fff"/></svg>
    <span class="band-url">www.veltorgroup.com</span>
  </div>
</section>

</body>
</html>
```